Home page design for Drone video business (the Business focusses on home videos for realtors)

Dear reader,

*I NEED DESIGNS OF ALL THE PAGES*
We need a first design of a homepage and of 4 other pages of the website of a business that sells drone video services. All the pages will need to be in the similar design style.
The video's are targeted at consumers that want to sell there home and would like to have a cool drone video of photos of their home.

How does the website look:
- has a navbar on top
- A cool looking banner of an areal drone.
- A Big header: with company name: SkyNestReels
- A smaller subheader: We film your home to increase your chances of sale
- Then a section with a Big header: How does it work
- In this section a place for a vimeo explainitory video
- Then a similar navbar styled bar with a phone number and a email address
- Then a section where the videos porfolio is displayed in a cool way
- Inside this sectiona header: Our work

- A section with header: Why us?
- 4 symbols here with a subheader and some lorum ipsum text underneath (see wireframe images)

- Under that a: Contact us
- where you can put in name, email, phone, message box and a send button

- At the bottom a footer with phone number and a fake address for now.

Be creative. Use creative but serious color.
Use a serious font. Make it a sharp design. Sharp lines. Not to dark design and not to light design.

The wireframes are the same kind of images.
PLEASE PUT IN DESIGNS OF ALL THE PAGES

Good luck

Target Market(s)

People that want to sell home and want to make a cool drone video or photos of their home.

Industry/Entity Type

Business

Contact Information for Business Card

Milo Brenning
milo@skynestreels.example
+31647283915

Logo Text

SkyNestReels

Number of Pages Required

1 page

Font styles to use
Sans Serif

Requirements
Must have
• All the sections as explained in the instructions.
• The nav bar should have an about us, services, portfolio and a contact us buttons.
• See instruction for details.
• Must include designs of the front page, contact us, our services, portfolio and contact us.
• If you do add some designs for the "about us", "services", "prices", "portfolio" and "contact us" pages, you make a way better chance of winning the competition.
Nice to have
• designs for the other pages as described at the Must haves. You make a better chance of winning if you include them. Look at the wireframes to see the mockups for those pages. think creative about what kind of sections and design should be included in those pages.
Should not have
• bad designs.

```html
<!DOCTYPE html>
<html lang="en">
<head>
<meta charset="utf-8">
<title>SkyNestReels – Home</title>
<link href="https://fonts.googleapis.com/css2?family=Raleway:wght@400;500;600;700&display=swap" rel="stylesheet">
<style>
:root{
  --blue:#2a9fd0;
  --blue-dark:#1f86b3;
  --nav:#232425;
  --ink:#333;
  --muted:#555;
  --grey-band:#e9eaea;
  --white:#fff;
  --paper:#fbfbfb;
}
*{margin:0;padding:0;box-sizing:border-box}
html,body{width:755px;height:1200px;overflow:hidden}
body{font-family:'Raleway',sans-serif;color:var(--ink);background:var(--white);position:relative}
.abs{position:absolute}

/* nav */
.topbar{left:0;top:0;width:755px;height:21px;background:var(--nav);z-index:2}
.brand{left:158px;top:3px;display:flex;align-items:center;gap:4px;color:var(--white);font-size:10px;font-weight:600}
.brand-dot{width:9px;height:9px;border-radius:50%;background:var(--blue)}
.menu{left:378px;top:0;display:flex;height:21px}
.menu a{color:var(--white);text-decoration:none;font-size:6.5px;font-weight:500;line-height:21px;padding:0 4.5px}
.menu a.active{background:var(--blue)}

/* hero */
.hero{left:0;top:21px;width:755px;height:280px}
.hero-text{left:0;top:187px;width:755px;text-align:center;color:var(--white)}
.hero-kicker{font-size:9.5px;letter-spacing:.3px}
.hero-title{font-size:14.5px;font-weight:700}
.hero-sub{font-size:7.5px;font-weight:500;margin-top:3px}
.hero-chevron{left:374px;top:289px}

/* how it works */
.how{left:0;top:298px;width:755px;height:195px;background:var(--paper)}
.tag-head{left:156px;top:321px}
.tag-head span{position:absolute;left:6px;top:2px;color:var(--white);font-size:8.5px;font-weight:500;white-space:nowrap}
.how-sub{left:156px;top:344px;color:var(--blue);font-size:5.5px;font-weight:700}
.how-copy{left:156px;top:355px;width:150px;font-size:5.2px;line-height:8.4px;color:var(--muted)}
.contact-line{left:156px;display:flex;align-items:center;gap:7px;font-size:7.5px;color:var(--ink)}
.btn{background:var(--blue);color:var(--white);font-size:6px;font-weight:500;display:flex;align-items:center;justify-content:center}
.video{left:337px;top:321px;width:261px;height:152px;background:linear-gradient(160deg,#6d7a5c,#3f4a3a 55%,#8d9872);overflow:hidden}
.video-title{left:37px;top:9px;color:var(--blue);font-size:7.5px;font-weight:700;white-space:nowrap}
.video-from{left:37px;top:23px;color:var(--white);font-size:4.5px}
.video-from b{color:var(--blue);font-weight:500}
.video-bar{left:6px;top:129px;width:250px;height:17px;background:rgba(0,0,0,.55)}

/* work */
.work{left:0;top:493px;width:755px;height:309px;background:var(--blue)}
.section-title{width:755px;left:0;text-align:center;font-size:14.5px;font-weight:500}
.filters{left:0;top:545px;width:755px;display:flex;justify-content:center;gap:13px;color:var(--white);font-size:6.5px;font-weight:600}
.grid{left:156px;top:571px;width:442px;display:grid;grid-template-columns:repeat(3,145px);grid-auto-rows:94px;gap:3px 3.5px}
.tile{border:1px solid rgba(255,255,255,.6)}
.pager{left:349px;top:774px}

/* why */
.why{left:0;top:802px;width:755px;height:175px}
.perk{width:110px;text-align:center}
.perk-label{position:relative;height:13px;margin:6px auto 0;color:var(--white);font-size:7px;font-weight:500;line-height:13px}
.perk-label svg{position:absolute;left:0;top:0}
.perk-label span{position:relative}
.perk-copy{font-size:5px;line-height:6px;color:var(--muted);margin-top:3px;padding:0 4px}

/* contact */
.h-col{font-size:14.5px;font-weight:500;color:var(--ink)}
.info-label{left:156px;display:flex;align-items:center;gap:4px;color:var(--blue);font-size:7px;font-weight:700}
.info-val{left:156px;font-size:6px;color:var(--muted);line-height:6px}
.social{left:156px;top:1146px;display:flex;gap:6px}
.social i{width:14px;height:14px;border-radius:50%;background:var(--blue);display:block}
.field{border-bottom:1px solid #999;height:10px;font-size:4.5px;color:var(--muted)}

/* footer */
.footer{left:0;top:1184px;width:755px;height:16px;background:var(--blue);color:var(--white);font-size:5px}
.footer-links{left:166px;top:5px;display:flex;gap:7px}
.footer-copy{left:492px;top:5px}
</style>
</head>
<body>

<header class="abs topbar">
  <div class="abs brand"><i class="brand-dot"></i>SkyNestReels</div>
  <nav class="abs menu">
    <a class="active">HOME</a><a>ABOUT US</a><a>SERVICES</a><a>PRICES</a><a>PORTFOLIO</a><a>CONTACT US</a>
  </nav>
</header>

<section class="abs hero" role="img" aria-label="Dusk photo of a brick family house with a camera drone hovering in front of it">
  <svg width="755" height="280" viewBox="0 0 755 280">
    <defs>
      <linearGradient id="heroSky" x1="0" y1="0" x2="0" y2="1">
        <stop offset="0" stop-color="#3f3e3f"/>
        <stop offset=".3" stop-color="#56473f"/>
        <stop offset=".62" stop-color="#6a5246"/>
        <stop offset=".78" stop-color="#3e3b33"/>
        <stop offset="1" stop-color="#2a2c28"/>
      </linearGradient>
      <radialGradient id="houseGlow" cx=".5" cy=".5" r=".5">
        <stop offset="0" stop-color="#8a6a56" stop-opacity=".75"/>
        <stop offset="1" stop-color="#8a6a56" stop-opacity="0"/>
      </radialGradient>
      <radialGradient id="droneShade" cx=".5" cy=".5" r=".5">
        <stop offset="0" stop-color="#161618" stop-opacity=".95"/>
        <stop offset=".55" stop-color="#1f1f21" stop-opacity=".6"/>
        <stop offset="1" stop-color="#1f1f21" stop-opacity="0"/>
      </radialGradient>
      <clipPath id="heroClip"><path d="M0 0H755V257L378 279L0 257Z"/></clipPath>
    </defs>
    <g clip-path="url(#heroClip)">
      <rect width="755" height="280" fill="url(#heroSky)"/>
      <ellipse cx="180" cy="140" rx="180" ry="90" fill="url(#houseGlow)"/>
      <ellipse cx="590" cy="140" rx="180" ry="90" fill="url(#houseGlow)"/>
      <ellipse cx="378" cy="160" rx="120" ry="50" fill="url(#houseGlow)"/>
      <ellipse cx="378" cy="100" rx="110" ry="70" fill="url(#droneShade)"/>
    </g>
    <path d="M0 257L378 279L755 257" fill="none" stroke="#2a9fd0" stroke-width="1.5"/>
  </svg>
</section>
<div class="abs hero-text">
  <div class="hero-kicker">WELCOME TO</div>
  <div class="hero-title">SKYNESTREELS</div>
  <div class="hero-sub">We Film Your Home To Increase Your Chances Of Sale</div>
</div>

<section class="abs how"></section>
<svg class="abs hero-chevron" width="8" height="5" viewBox="0 0 8 5"><path d="M1 1L4 4L7 1" fill="none" stroke="#444" stroke-width="1"/></svg>
<div class="abs tag-head">
  <svg width="157" height="15" viewBox="0 0 157 15"><path d="M0 0H145L157 15H0Z" fill="#2a9fd0"/></svg>
  <span>HOW DOES IT WORK ?</span>
</div>
<div class="abs how-sub">VIDEO QUALITY</div>
<p class="abs how-copy">Lorem Ipsum is simply dummy text of the printing and type-setting industry. Lorem Ipsum has been the industry's standard dummy text ever since the 1500s, when an unknown printer took a...</p>
<div class="abs contact-line" style="top:408px">
  <svg width="7" height="5" viewBox="0 0 7 5"><rect width="7" height="5" fill="#2a9fd0"/><path d="M0 0L3.5 3L7 0" fill="none" stroke="#fff" stroke-width=".7"/></svg>
  hello@skynestreels.example
</div>
<div class="abs contact-line" style="top:431px">
  <svg width="7" height="7" viewBox="0 0 7 7"><path d="M1 0L2.6 1.6L1.8 2.7Q3 4.6 4.3 5.2L5.4 4.4L7 6L5.8 7Q1.5 5.8 0 1.2Z" fill="#2a9fd0"/></svg>
  +31652904176
</div>
<div class="abs btn" style="left:156px;top:456px;width:63px;height:14px">CONTACT US</div>

<div class="abs video" role="img" aria-label="Explainer video still of a camera drone in flight">
  <div class="abs video-title">Place Title For Movie Here</div>
  <div class="abs video-from">from <b>Your Channel</b></div>
  <div class="abs video-bar"></div>
  <svg class="abs" style="left:12px;top:133px" width="240" height="10" viewBox="0 0 240 10">
    <path d="M4 1L11 5L4 9Z" fill="#fff"/>
    <rect x="38" y="4" width="165" height="2" fill="#666"/>
    <rect x="38" y="4" width="75" height="2" fill="#2a9fd0"/>
  </svg>
</div>

<section class="abs work"></section>
<h2 class="abs section-title" style="top:510px;color:var(--white)">OUR WORK</h2>
<div class="abs filters"><span>HOME</span><span>OFFICE</span><span>TRAVEL</span><span>HOTEL</span></div>
<div class="abs grid">
  <div class="tile" role="img" aria-label="Drone pilot preparing a flight outside a house" style="background:linear-gradient(160deg,#3d4650,#4a4639)"></div>
  <div class="tile" role="img" aria-label="Drone flying above a city" style="background:linear-gradient(160deg,#8f9aa0,#6a6e67)"></div>
  <div class="tile" role="img" aria-label="Aerial view of a house among trees" style="background:linear-gradient(160deg,#3e5a34,#8c9fae)"></div>
  <div class="tile" role="img" aria-label="Aerial view of a villa on a green slope" style="background:linear-gradient(160deg,#5f7440,#b69a7c)"></div>
  <div class="tile" role="img" aria-label="Aerial view of a modern house with pool" style="background:linear-gradient(160deg,#4f6142,#6c7d86)"></div>
  <div class="tile" role="img" aria-label="Aerial view of a coastal mansion" style="background:linear-gradient(160deg,#8da0b4,#bfa986 60%,#4d6a3e)"></div>
</div>
<svg class="abs pager" width="58" height="16" viewBox="0 0 58 16">
  <path d="M5 0H58L53 16H0Z" fill="#fff"/>
  <path d="M31 1L27 15" stroke="#2a9fd0" stroke-width=".8"/>
  <path d="M19 4L15 8L19 12M40 4L44 8L40 12" fill="none" stroke="#2a9fd0" stroke-width="1.2"/>
</svg>

<section class="abs why">
  <svg width="755" height="175" viewBox="0 0 755 175"><path d="M0 0H755V153L378 174L0 153Z" fill="#e9eaea"/></svg>
</section>
<h2 class="abs section-title" style="top:818px">WHY US</h2>

<div class="abs perk" style="left:149px;top:858px">
  <svg width="38" height="38" viewBox="0 0 38 38"><circle cx="19" cy="19" r="18" fill="none" stroke="#2a9fd0" stroke-width="1.6"/><text x="19" y="27" text-anchor="middle" font-family="Raleway,sans-serif" font-size="24" font-weight="700" fill="#2a9fd0">$</text></svg>
  <div class="perk-label" style="width:64px"><svg width="64" height="13"><path d="M5 0H64L59 13H0Z" fill="#2a9fd0"/></svg><span>Cheap</span></div>
  <p class="perk-copy">Lorem Ipsum is simply dummy text of the printing and typesetting industry. Lorem Ipsum has been the</p>
</div>
<div class="abs perk" style="left:269px;top:858px">
  <svg width="38" height="38" viewBox="0 0 38 38"><circle cx="19" cy="19" r="18" fill="none" stroke="#2a9fd0" stroke-width="1.6"/><path d="M11 24A8 8 0 1 1 27 24" fill="none" stroke="#2a9fd0" stroke-width="3"/><circle cx="19" cy="24" r="2" fill="#2a9fd0"/></svg>
  <div class="perk-label" style="width:64px"><svg width="64" height="13"><path d="M5 0H64L59 13H0Z" fill="#2a9fd0"/></svg><span>Flexible</span></div>
  <p class="perk-copy">Lorem Ipsum is simply dummy text of the printing and typesetting industry. Lorem Ipsum has been the</p>
</div>
<div class="abs perk" style="left:383px;top:858px">
  <svg width="38" height="38" viewBox="0 0 38 38"><circle cx="19" cy="19" r="18" fill="none" stroke="#2a9fd0" stroke-width="1.6"/><circle cx="19" cy="15" r="7" fill="#2a9fd0"/><circle cx="19" cy="15" r="3" fill="#fff"/><path d="M14 20L12 29L16 27L19 30L22 27L26 29L24 20Z" fill="#2a9fd0"/></svg>
  <div class="perk-label" style="width:64px"><svg width="64" height="13"><path d="M5 0H64L59 13H0Z" fill="#2a9fd0"/></svg><span>Quality</span></div>
  <p class="perk-copy">Lorem Ipsum is simply dummy text of the printing and typesetting industry. Lorem Ipsum has been the</p>
</div>
<div class="abs perk" style="left:495px;top:858px">
  <svg width="38" height="38" viewBox="0 0 38 38"><circle cx="19" cy="19" r="18" fill="none" stroke="#2a9fd0" stroke-width="1.6"/><path d="M12 26H26M13 25V22H15V25M17 25V19H19V25M21 25V16H23V25M25 25V12" stroke="#2a9fd0" stroke-width="1.4" fill="none"/></svg>
  <div class="perk-label" style="width:98px;margin-left:-6px"><svg width="98" height="13"><path d="M5 0H98L93 13H0Z" fill="#2a9fd0"/></svg><span>Increase Sale Chance</span></div>
  <p class="perk-copy">Lorem Ipsum is simply dummy text of the printing and typesetting industry. Lorem Ipsum has been the</p>
</div>

<h2 class="abs h-col" style="left:156px;top:995px">ADDRESS</h2>
<div class="abs info-label" style="top:1027px"><svg width="4" height="7"><rect x=".5" y=".5" width="3" height="6" rx=".6" fill="none" stroke="#2a9fd0"/></svg>Phone :</div>
<div class="abs info-val" style="top:1041px">+31652904176</div>
<div class="abs info-label" style="top:1063px"><svg width="7" height="5"><rect width="7" height="5" fill="#2a9fd0"/><path d="M0 0L3.5 3L7 0" fill="none" stroke="#fff" stroke-width=".7"/></svg>Email :</div>
<div class="abs info-val" style="top:1075px">hello@skynestreels.example</div>
<div class="abs info-label" style="top:1097px"><svg width="5" height="7"><path d="M2.5 7L0.4 3.2A2.3 2.3 0 1 1 4.6 3.2Z" fill="#2a9fd0"/><circle cx="2.5" cy="2.3" r=".8" fill="#fff"/></svg>Address :</div>
<div class="abs info-val" style="top:1110px">PO Box 4410 Harbour Lane<br>East Linden 3021 Netherlands</div>
<div class="abs social"><i></i><i></i><i></i></div>

<h2 class="abs h-col" style="left:332px;top:995px">CONTACT US</h2>
<div class="abs field" style="left:332px;top:1021px;width:122px">Name :</div>
<div class="abs field" style="left:463px;top:1021px;width:135px">Email :</div>
<div class="abs field" style="left:332px;top:1053px;width:266px">Phone :</div>
<div class="abs field" style="left:332px;top:1117px;width:266px">Message :</div>
<div class="abs btn" style="left:332px;top:1146px;width:63px;height:14px">CONTACT US</div>

<footer class="abs footer">
  <div class="abs footer-links"><span>HOME</span><span>ABOUT US</span><span>SERVICES</span><span>PRICES</span><span>PORTFOLIO</span><span>CONTACT US</span></div>
  <div class="abs footer-copy">Copyright © 2016. All rights reserved</div>
</footer>

</body>
</html>
```